Law firm website marketed direct to many individual clients

I need someone to design a very basic website for a law firm that will be very eye catching. It's going to be a single-paged, scrolling website with a small number of folds. I have uploaded a simple word document that outlines the basics of what I thought could be the layout, but I am open to suggestion on font, size, shades of color, organization, etc. etc. Essentially the website just needs to be a very efficient and visually appealing way of conveying some simple messages.

Target Market(s)

High volumes of individuals who have gotten into a car accident and then google on their phones a lawyer to hire to represent them.

Industry/Entity Type

Legal

Number of Pages Required

1 page

Font styles to use
Serif
Sans Serif

Colors
34a7d7
85cae6
0592cd

Requirements
Must have
• Must be bright and grab the users attention with color scheme and layout. The different sections should be done in such a way that they can fit entirely onto one smart phone or tablet screen.
Nice to have
• I'd like to try and see what it looks like if in the middle somewhere there is a fold that says "MEET YOUR ATTORNEYS" and includes individual photos of two attorneys, one on the left side and one on the right. And then a small bio section on them. I don't want the photos to include a square or rectangle background, I want the person in the photo to be superimposed on top of whatever pattern or background you have in the fold.
Should not have
• Do not want too much text. Anything more than 2 sentences in any single place is unacceptable.

```html
<!DOCTYPE html>
<html lang="en">
<head>
<meta charset="utf-8">
<title>Harbor Point Law Group</title>
<link href="https://fonts.googleapis.com/css2?family=Raleway:wght@400;500;600;700&display=swap" rel="stylesheet">
<style>
:root{
  --brand:#0592cd;
  --accent:#34a7d7;
  --light:#85cae6;
  --band-center:#30baec;
  --band-edge:#0a3d63;
  --text-grey:#555;
  --white:#fff;
}
*{margin:0;padding:0;box-sizing:border-box}
html,body{width:1043px;height:1200px;overflow:hidden}
body{font-family:'Raleway',sans-serif;background:var(--white);position:relative}
.abs{position:absolute}
.center{left:0;width:1043px;text-align:center}

.site-header{top:0;left:0;width:1043px;height:62px;border-top:3px solid var(--light);background:var(--white)}
.brand-name{left:114px;top:16px;font-size:21px;font-weight:700;color:var(--brand)}
.header-call{left:770px;top:13px;display:flex;align-items:center;gap:6px;color:var(--brand)}
.header-call svg{width:27px;height:27px;color:var(--brand)}
.header-call .label{font-size:13px;font-weight:600;line-height:15px}
.header-call .number{font-size:19px;font-weight:700;line-height:22px}

.band{left:0;width:1043px;background:radial-gradient(ellipse 62% 120% at 50% 75%,var(--band-center) 0%,#1d9ad6 45%,#0f6aa3 78%,var(--band-edge) 100%)}
.hero{top:62px;height:240px}
.cta-band{top:755px;height:301px}

.hero-title{font-size:39px;font-weight:400;color:var(--white);line-height:46px}

.call-btn{left:426px;width:191px;height:47px;border:2px solid var(--white);display:flex;align-items:center;justify-content:center;gap:8px;color:var(--white);font-size:19px;font-weight:700}
.call-btn svg{width:28px;height:28px}
.call-btn.outline-blue{border-color:var(--brand);color:var(--brand)}

.benefit-title{font-size:39px;font-weight:400;color:var(--accent);line-height:44px}
.benefit-text{font-size:14px;color:var(--text-grey);line-height:18px}

.cta-title{font-size:39px;font-weight:400;color:var(--white);line-height:44px}
.cta-text{font-size:14px;color:var(--white);line-height:24px}

.site-footer{top:1056px;left:0;width:1043px;height:144px;background:var(--brand);border-top:2px solid var(--light);color:var(--white)}
.footer-name{font-size:13px;font-weight:700}
.footer-address{font-size:13px}
.footer-call{left:0;width:1043px;display:flex;justify-content:center;align-items:center;gap:8px;font-size:19px;font-weight:700}
.footer-call svg{width:28px;height:28px}
.copyright{font-size:11.5px;color:#dff1fa}
</style>
</head>
<body>
<svg width="0" height="0" style="position:absolute">
  <defs>
    <symbol id="phone-icon" viewBox="0 0 24 24">
      <circle cx="12" cy="12" r="10.6" fill="none" stroke="currentColor" stroke-width="1.4"/>
      <path d="M10.2 5.6c-1.3.6-2.3 2.3-2 4.6.4 3.2 2.5 6.4 4.8 7.6 1.1.6 2 .3 2.6-.3l.5-.6-2-2.3-1.1.5c-.9-.6-2-2.8-2-4l1.1-.6-.2-3.1z" fill="currentColor"/>
    </symbol>
  </defs>
</svg>

<header class="site-header abs">
  <div class="brand-name abs">Harbor Point Law Group</div>
  <div class="header-call abs">
    <svg><use href="#phone-icon"/></svg>
    <div><div class="label">Call Us Today</div><div class="number">504-555-0142</div></div>
  </div>
</header>

<section class="hero band abs">
  <h1 class="hero-title abs center" style="top:36px">Accident? Injured?</h1>
  <h2 class="hero-title abs center" style="top:91px">Your Case, Your Money</h2>
  <div class="call-btn abs" style="top:154px"><svg><use href="#phone-icon"/></svg>504-555-0142</div>
</section>

<section class="benefits">
  <h2 class="benefit-title abs center" style="top:332px">Low Fees</h2>
  <p class="benefit-text abs center" style="top:373px">We charge less, so you keep more.</p>
  <h2 class="benefit-title abs center" style="top:419px">Free Consultation</h2>
  <p class="benefit-text abs center" style="top:460px">It's always free to talk to us.</p>
  <h2 class="benefit-title abs center" style="top:504px">Get Started Using Only Your Phone</h2>
  <p class="benefit-text abs center" style="top:545px">No need to come to the office, sign up using your phone.</p>
  <h2 class="benefit-title abs center" style="top:588px">Speak Directly To A Lawyer</h2>
  <p class="benefit-text abs center" style="top:628px">No staff screening. Talk right to a lawyer on your first call.</p>
  <div class="call-btn outline-blue abs" style="top:670px"><svg><use href="#phone-icon"/></svg>504-555-0142</div>
</section>

<section class="cta-band band abs">
  <h2 class="cta-title abs center" style="top:36px">No Fee Unless We Win</h2>
  <p class="cta-text abs center" style="top:72px">We don't get paid unless you get paid. It's as simple as that. We let our results do the talking for us.</p>
  <h2 class="cta-title abs center" style="top:116px">Questions About Anything?</h2>
  <p class="cta-text abs" style="top:155px;left:110px;width:823px;text-align:center">We're here to help. Feel free to call us at 504-555-0142 to speak to one of our attorneys. With extensive experience in helping clients get the results that they want, our team is always just a phone call away.</p>
  <div class="call-btn abs" style="top:216px"><svg><use href="#phone-icon"/></svg>504-555-0142</div>
</section>

<footer class="site-footer abs">
  <div class="footer-name abs center" style="top:24px">Harbor Point Law Group</div>
  <div class="footer-address abs center" style="top:47px">Sample Office Suite, New Orleans, LA 70130</div>
  <div class="footer-call abs" style="top:70px"><svg><use href="#phone-icon"/></svg>504-555-0142</div>
  <div class="copyright abs center" style="top:114px">Copyright © 2016 HarborPointLawGroup . All Rights Reserved.</div>
</footer>
</body>
</html>
```